Flyer to acquire new customers for a craft business

Create an A5 (4 pages in total) flyer describing proposed services from a craft business to new customers.

Services are :

All types of renovation (painting, plastering, attaching wallpapers ....)
All types of repairs
Electric repairs
Little to medium woodworks
Services around the house and garden

Flyer must be translatable into several languages beginning with FRENCH.
Texts are being written by ourselves.

Target Market(s)

Private customers

Industry/Entity Type

Mixed craft business

Colors

Designer to choose colors to be used in the design.

```html
<!DOCTYPE html>
<html lang="fr">
<head>
<meta charset="utf-8">
<title>Atelier Maréchal – Dépliant A5</title>
<link rel="stylesheet" href="https://fonts.googleapis.com/css2?family=Open+Sans:ital,wght@0,400;0,600;0,700;1,400&family=Roboto:wght@300;400;500;700&display=swap">
<style>
  :root{
    --ink:#2b2150;
    --ink-deep:#231a44;
    --gold:#f4a51c;
    --paper:#ffffff;
    --cream:#fdf1e4;
    --text:#222;
    --muted:#555;
    --stage:#ececec;
  }
  *{box-sizing:border-box;margin:0;padding:0}
  html,body{width:1200px;height:638px;overflow:hidden;background:var(--stage)}
  body{position:relative;font-family:"Open Sans",sans-serif;color:var(--text)}
  .spread{position:absolute;top:111px;width:584px;height:416px;display:flex;box-shadow:0 2px 8px rgba(0,0,0,.12)}
  .spread--outer{left:10px}
  .spread--inner{left:606px}
  .page{position:relative;width:292px;height:416px;overflow:hidden;background:var(--paper)}
  .page--dark{background:linear-gradient(160deg,#2f2557 0%,var(--ink-deep) 100%);color:#fff}
  .abs{position:absolute}
  .photo{position:absolute}

  /* back cover */
  .hero-band{left:0;top:0;width:292px;height:58px;background:var(--ink);color:#fff;
    font-family:"Roboto",sans-serif;font-weight:300;font-size:13.5px;line-height:16px;text-align:center;padding-top:13px;letter-spacing:.4px}
  .hero-band strong{color:var(--gold);font-weight:700}
  .intro{left:0;top:74px;width:292px;text-align:center;font-size:7.6px;line-height:10.5px}
  .intro em{font-style:italic}
  .cta{left:0;top:118px;width:292px;text-align:center;font-weight:600;font-size:11px}
  .brand-mark{left:121px;top:284px;width:50px;height:50px;border-radius:50%;background:var(--ink);border:3px solid #fff}
  .brand-name{left:0;top:338px;width:292px;text-align:center;font-weight:700;font-size:7.8px;color:var(--ink)}
  .contact{font-size:5.6px;line-height:8.5px;color:#333}
  .contact .ico{color:var(--gold);margin-right:2px}
  .hours{font-size:4.6px;color:#333}
  .web-rule{left:0;width:292px;display:flex;align-items:center;gap:6px;font-size:5.2px}
  .web-rule::before,.web-rule::after{content:"";flex:1;height:.7px;background:currentColor}

  /* front cover */
  .front-brand{left:56px;top:36px;display:flex;align-items:center;gap:12px}
  .front-brand .dot{width:56px;height:56px;border-radius:50%;background:var(--ink)}
  .front-brand span{font-weight:700;font-size:15px;color:var(--ink)}
  .promise{left:0;top:118px;width:292px;height:64px;background:var(--ink);padding:4px}
  .promise div{height:100%;border:1px solid #cfc8e8;color:var(--gold);font-family:"Roboto",sans-serif;font-weight:700;
    font-size:13.6px;line-height:17px;text-align:center;padding-top:10px;letter-spacing:.2px}
  .footer-strip{left:0;top:392px;width:292px;height:24px;background:var(--ink);color:#fff;padding:0 4px;padding-top:9px}

  /* inner left */
  .about{left:25px;top:20px;width:250px;font-family:"Roboto",sans-serif;font-size:6.4px;line-height:9px;color:#fff}
  .about .hl{color:var(--gold)}
  .about ul{list-style:none;margin:2px 0}
  .about li::before{content:"";display:inline-block;width:4px;height:4px;border-radius:50%;background:var(--gold);margin-right:4px}
  .about p+p{margin-top:7px}
  .feature{left:0;width:292px;text-align:center;font-family:"Roboto",sans-serif;font-weight:500;font-size:6.8px;color:#fff}
  .feature svg{display:block;margin:0 auto 6px}

  /* inner right */
  .crafts-title{left:0;top:24px;width:292px;text-align:center;font-family:"Roboto",sans-serif;font-weight:500;font-size:13px;
    color:var(--ink);text-decoration:underline;text-underline-offset:3px;letter-spacing:.3px}
  .backing{background:var(--cream)}
  .svc-h{font-family:"Roboto",sans-serif;font-weight:500;color:var(--gold);font-size:10.5px;line-height:11px}
  .svc-p{font-family:"Roboto",sans-serif;font-size:5.3px;line-height:6.8px;color:#333;text-align:justify}
</style>
</head>
<body>

<section class="spread spread--outer">
  <!-- back cover -->
  <article class="page">
    <header class="abs hero-band">VOUS ÊTES À LA RECHERCHE<br>D’UN PARTENAIRE <strong>FIABLE</strong></header>
    <p class="abs intro">Pour tous types de travaux et de services de l’artisanat<br>petit, moyens et aussi <strong>plus grands</strong><br><em>Intervention rapide</em></p>
    <p class="abs cta">Contactez-nous pour un conseil personnalisé</p>
    <div class="photo" role="img" aria-label="Atelier de menuiserie rempli de planches de bois empilées" style="left:0;top:135px;width:292px;height:176px;background:linear-gradient(135deg,#8a6e54 0%,#c9a583 45%,#a98263 70%,#6f5a48 100%)"></div>
    <div class="abs brand-mark"></div>
    <p class="abs brand-name">Atelier Maréchal</p>
    <div class="abs contact" style="left:42px;top:352px"><span class="ico">⚲</span>12, rue des Artisans<br>&nbsp;&nbsp;&nbsp;4100 Valmont</div>
    <div class="abs contact" style="left:185px;top:352px"><span class="ico">✆</span>21 40 55 18<br><span class="ico">●</span>www.ateliermarechal.lu<br><span class="ico">✉</span>info@ateliermarechal.lu</div>
    <p class="abs hours" style="left:50px;top:383px">Monday – Friday 9 am to 7 pm</p>
    <p class="abs hours" style="left:185px;top:383px">Saturday 8 am to 1 pm</p>
    <p class="abs web-rule" style="top:395px;padding:0 2px;color:var(--ink)">www.ateliermarechal.lu</p>
  </article>

  <!-- front cover -->
  <article class="page">
    <div class="abs front-brand"><span class="dot"></span><span>Atelier Maréchal</span></div>
    <div class="abs promise"><div>Nous réalisons tous vos travaux<br>intérieurs et extérieurs</div></div>
    <div class="photo" role="img" aria-label="Meuleuse projetant des étincelles sur une pièce de métal" style="left:5px;top:188px;width:138px;height:82px;background:linear-gradient(135deg,#2a2d33 0%,#55606b 55%,#d98a2c 100%)"></div>
    <div class="photo" role="img" aria-label="Clés et outils métalliques posés sur un établi" style="left:149px;top:188px;width:138px;height:82px;background:linear-gradient(135deg,#3a3c40 0%,#8c8f94 50%,#4a4c50 100%)"></div>
    <div class="photo" role="img" aria-label="Main gantée choisissant une clé sur un panneau d’outils bleu" style="left:5px;top:276px;width:282px;height:94px;background:linear-gradient(120deg,#173f78 0%,#2f63a8 45%,#8b8f96 70%,#1c3d6e 100%)"></div>
    <div class="abs footer-strip"><p class="web-rule" style="position:static;color:#fff">www.ateliermarechal.lu</p></div>
  </article>
</section>

<section class="spread spread--inner">
  <!-- inner left -->
  <article class="page page--dark">
    <div class="abs about">
      <p><span class="hl">«Atelier Maréchal»</span> est une société jeune et dynamique, actif dans le secteur de l’artisanat. Nous proposons des services en général dans le domaine de la construction et de l’habitat.</p>
      <ul>
        <li>Une réparation ?</li>
        <li>Une modification ?</li>
        <li>Besoin de support technique ou d’un coup de main ?</li>
      </ul>
      <p style="margin-top:0">Un simple coup de fil suffit pour une prise en charge professionnelle.</p>
      <p style="margin-top:14px">«Atelier Maréchal» vous propose ses services, que ce soit pour votre habitat, les alentours ou votre société. Flexible et rapide.</p>
    </div>

    <div class="abs feature" style="top:150px">
      <svg width="50" height="56" viewBox="0 0 50 56" aria-hidden="true">
        <polygon points="25,2 47,15 47,41 25,54 3,41 3,15" fill="#fff" stroke="#f4a51c" stroke-width="2"/>
        <path d="M15 38 L33 20 M33 20 l3 -4 M17 18 L35 36" stroke="#f4a51c" stroke-width="3" stroke-linecap="round" fill="none"/>
        <path d="M15 38 L33 20 M17 18 L35 36" stroke="#2b2150" stroke-width="1" fill="none"/>
      </svg>
      Réparations de tout genre
    </div>
    <div class="abs feature" style="top:234px">
      <svg width="50" height="56" viewBox="0 0 50 56" aria-hidden="true">
        <polygon points="25,2 47,15 47,41 25,54 3,41 3,15" fill="#fff" stroke="#f4a51c" stroke-width="2"/>
        <rect x="13" y="17" width="14" height="12" fill="none" stroke="#2b2150" stroke-width="1.3"/>
        <rect x="22" y="26" width="14" height="12" fill="none" stroke="#2b2150" stroke-width="1.3"/>
        <path d="M16 23 l3 3 5 -6 M25 32 l3 3 5 -6" stroke="#f4a51c" stroke-width="2" fill="none" stroke-linecap="round"/>
      </svg>
      Services professionnels
    </div>
    <div class="abs feature" style="top:318px">
      <svg width="50" height="56" viewBox="0 0 50 56" aria-hidden="true">
        <polygon points="25,2 47,15 47,41 25,54 3,41 3,15" fill="#fff" stroke="#f4a51c" stroke-width="2"/>
        <rect x="22" y="15" width="16" height="11" rx="3" fill="none" stroke="#2b2150" stroke-width="1.3"/>
        <circle cx="26" cy="20.5" r="1.3" fill="#f4a51c"/><circle cx="30" cy="20.5" r="1.3" fill="#f4a51c"/><circle cx="34" cy="20.5" r="1.3" fill="#f4a51c"/>
        <path d="M14 24 q-2 4 3 10 q6 6 10 4 l2 -3 -4 -3 -2 2 q-4 -2 -6 -6 l2 -2 -3 -4 z" fill="none" stroke="#2b2150" stroke-width="1.3"/>
      </svg>
      Support dans les meilleurs délais
    </div>
  </article>

  <!-- inner right -->
  <article class="page">
    <h2 class="abs crafts-title">ÄREN HANDWRIERKER</h2>

    <div class="abs backing" style="left:16px;top:68px;width:104px;height:104px"></div>
    <div class="photo" role="img" aria-label="Pinceaux, rouleau et ruban de peintre pour la rénovation" style="left:23px;top:74px;width:104px;height:82px;border-radius:3px;background:linear-gradient(135deg,#8c5a2f 0%,#e0a64a 45%,#3f6f73 100%)"></div>
    <h3 class="abs svc-h" style="left:151px;top:76px">Rénovations</h3>
    <p class="abs svc-p" style="left:152px;top:93px;width:124px">Nous proposons tous types de rénovations (petite, moyenne ou grande envergure).<br>peinture, carrelage, plâtrage, murs en placo-plâtre, sanitaire.<br>Nous utilisons des produits standards bien connus mais de même des produits naturels comme l’argile et bien d’autre.</p>

    <h3 class="abs svc-h" style="left:16px;top:182px">Réparations</h3>
    <p class="abs svc-p" style="left:16px;top:202px;width:124px;text-align:left">Une fuite d’eau? un remplacement d’un tuyau ou même une extension sanitaire?<br>Remplacer du carrelage défectueux même des petits travaux ?<br>Une réparation d’un garde-corps ?<br>Le remplacement d’une porte intérieure ?<br>Presque tout est possible</p>
    <div class="abs backing" style="left:172px;top:182px;width:104px;height:104px"></div>
    <div class="photo" role="img" aria-label="Main tenant des pinces devant une caisse à outils" style="left:151px;top:189px;width:104px;height:82px;border-radius:3px;background:linear-gradient(135deg,#1d1f24 0%,#5b5f66 50%,#e2b23a 100%)"></div>

    <div class="abs backing" style="left:16px;top:296px;width:104px;height:104px"></div>
    <div class="photo" role="img" aria-label="Matériel d’électricien : câbles, multimètre et ruban isolant" style="left:23px;top:302px;width:104px;height:82px;border-radius:3px;background:linear-gradient(135deg,#f0c23a 0%,#d9d9d9 40%,#2f7fc1 70%,#c9302c 100%)"></div>
    <h3 class="abs svc-h" style="left:151px;top:304px">Travaux en<br>électricité</h3>
    <p class="abs svc-p" style="left:152px;top:332px;width:124px">Installation de lampadaires, remplacement et extensions de circuits électriques, dépannages en électricité, systèmes d’alarme et de vidéosurveillance ne sont quelques exemples de notre savoir faire.</p>
  </article>
</section>

</body>
</html>
```